Door Hanger Design for Electricians Serving Homes

I would like our logo incorporated into the door hanger. We would like a place for a tear off section on the bottom of the hanger with our contact information: K&T Electric - (555) 318-4702 - www.kandtelectric.example - info@kandtelectric.example.
Door Hanger Script
Front Side of the Door Hanger:
[Company Logo]
Need a Reliable Electrician?
Your Local Electrical Expert is Just Around the Corner!
• Quick Response Times
• Affordable Rates
• Quality Workmanship
• Fully Licensed & Insured
• Special Offer:
• 10% OFF Your First Service Call!
Back Side of the Door Hanger:
Don't Let Electrical Issues Keep You in the Dark!
From flickering lights to complete system upgrades, we've got all your
residential electrical needs covered. Our services include:
• Electrical Repairs & Troubleshooting
• Lighting Installation & Upgrades
• Safety Inspections & Code Compliance
• Energy-Efficient Solutions
• 24/7 Emergency Services
• Why Choose Us?
• Friendly, Local Service
• Over 30 Years of Experience
• Satisfaction Guaranteed
• Upfront Pricing
Call Us Today: [Your Phone Number]
Visit Our Website: [Your Website]
Book Your Appointment Now and Claim Your 10% Discount!
Offer valid for new customers on the first visit only. Mention this door hanger when
booking.
[Your Company Name and Contact Information]
Follow Us on Social Media for More Tips and Special Offers!
[Icons for social media platforms: Chatterpage, Pixmosaic, Quibbler, etc.]
Design Tips:
Use bold, clear fonts for easy reading.
Incorporate your brand colors and logo for instant recognition.
Include a clear call to action (CTA) on both sides.
Add a tear-off section at the bottom with your contact information for
convenience.
Use high-quality images or graphics related to electrical work to catch
the eye.
This door hanger design and copy aim to attract residential clients by
highlighting the benefits of your electrical services, special offers, and
how they can easily get in touch with you for their electrical needs.
The door knocker template will have three of the same design on front and three of the same design on the back. This template is from the print shop.

```html
<!DOCTYPE html>
<html lang="en">
<head>
<meta charset="utf-8">
<title>K&amp;T Electric Door Hangers</title>
<link href="https://fonts.googleapis.com/css2?family=Montserrat:wght@400;600;700;800&family=Source+Sans+3:wght@400;600&display=swap" rel="stylesheet">
<style>
  :root {
    --backdrop: #dcdcdc;
    --ink: #000000;
    --paper: #ffffff;
    --brand-red: #d0141a;
    --lamp-dark: #1a1410;
    --lamp-warm: #6b5a40;
    --panel-grey: #8a8f96;
    --panel-blue: #5c6f86;
    --worker-blue: #8fa8c2;
    --bulb-rose: #b88a78;
  }
  * { margin: 0; padding: 0; box-sizing: border-box; }
  html, body { width: 1200px; height: 1200px; overflow: hidden; background: var(--backdrop); }
  body { position: relative; font-family: "Montserrat", sans-serif; color: var(--ink); }

  .hanger {
    position: absolute; top: 124px; width: 405px; height: 952px;
    background: var(--paper); overflow: hidden;
    box-shadow: 6px 8px 10px rgba(0,0,0,0.35);
  }
  .hanger--front { left: 170px; }
  .hanger--back { left: 625px; }
  .hanger > * { position: absolute; }

  .door-hole {
    width: 112px; height: 112px; border-radius: 50%;
    left: 146px; top: 70px; background: var(--backdrop);
    box-shadow: inset 2px 3px 5px rgba(0,0,0,0.35); z-index: 3;
  }
  .photo { left: 0; }
  .photo--lamps {
    top: 0; width: 405px; height: 308px;
    background: radial-gradient(ellipse at 60% 45%, var(--lamp-warm), var(--lamp-dark) 70%);
  }
  .photo--panel {
    top: 0; width: 405px; height: 227px;
    background: linear-gradient(120deg, #c9ccd0 0%, var(--panel-grey) 40%, var(--panel-blue) 75%, #3a3f46 100%);
  }
  .photo--worker {
    left: 190px; top: 534px; width: 215px; height: 311px;
    background: linear-gradient(90deg, var(--paper) 0%, #dfe6ee 25%, var(--worker-blue) 60%, #5b6f9c 100%);
  }
  .photo--bulbs {
    left: 262px; top: 560px; width: 143px; height: 174px;
    background: linear-gradient(160deg, #d9b3a0 0%, var(--bulb-rose) 50%, #6d4a3e 100%);
  }

  .brand {
    font-family: "Montserrat", sans-serif; font-weight: 800;
    font-size: 19px; line-height: 1.1; letter-spacing: 0.5px;
  }
  .brand--light { color: var(--paper); left: 45px; top: 248px; width: 120px; }
  .brand--dark { color: var(--ink); width: 100px; }

  .band { left: 0; width: 405px; background: var(--ink); color: var(--paper); text-align: center; }
  .headline { font-weight: 800; line-height: 1.1; }
  .front-headline { top: 308px; height: 122px; padding-top: 16px; font-size: 40px; }
  .back-headline { top: 227px; height: 139px; padding-top: 10px; font-size: 34px; line-height: 1.03; }

  .subhead {
    left: 0; width: 405px; text-align: center; top: 453px;
    font-weight: 700; font-size: 23px; line-height: 1.3; letter-spacing: 0.3px;
  }
  .intro {
    left: 0; width: 405px; text-align: center; top: 376px;
    font-weight: 700; font-size: 17px; line-height: 1.32; letter-spacing: 0.3px;
  }
  .services-title {
    left: 0; width: 405px; text-align: center; top: 458px;
    color: var(--brand-red); font-weight: 700; font-size: 18px; letter-spacing: 0.3px;
  }

  .bolt-list { list-style: none; font-family: "Source Sans 3", sans-serif; z-index: 2; }
  .bolt-list li { position: relative; padding-left: 16px; }
  .bolt-list li::before {
    content: ""; position: absolute; left: 0; top: 5px; width: 13px; height: 13px;
    background: var(--brand-red);
    clip-path: polygon(15% 0, 60% 35%, 45% 45%, 100% 100%, 30% 60%, 45% 50%, 0 15%);
  }
  .benefits { left: 28px; top: 539px; font-size: 18px; line-height: 22.4px; }
  .services { left: 27px; top: 491px; font-size: 18px; line-height: 22.4px; }

  .offer { left: 45px; top: 662px; font-weight: 700; font-size: 16px; line-height: 1.3; z-index: 2; }
  .offer .offer-big { display: block; color: var(--brand-red); font-weight: 800; font-size: 25px; line-height: 1.05; }

  .why { left: 35px; top: 646px; font-weight: 700; font-size: 16px; line-height: 22.4px; }

  .booking { left: 146px; top: 737px; font-weight: 700; font-size: 16px; line-height: 1.4; }
  .booking .offer-big { color: var(--brand-red); font-weight: 800; font-size: 24px; }
  .fine-print { left: 141px; top: 792px; font-family: "Source Sans 3", sans-serif; font-size: 10px; line-height: 1.35; }

  .footer { top: 845px; height: 107px; }
  .cta-pill {
    left: 120px; top: 827px; width: 165px; height: 33px; border-radius: 17px;
    background: var(--brand-red); color: var(--paper); z-index: 3;
    font-weight: 700; font-size: 21px; line-height: 33px; text-align: center; letter-spacing: 0.5px;
  }
  .phone { left: 0; width: 405px; top: 863px; text-align: center; color: var(--paper); font-weight: 700; font-size: 32px; letter-spacing: 0.5px; }
  .web-label { left: 0; width: 405px; top: 896px; text-align: center; color: var(--paper); font-size: 13px; letter-spacing: 0.5px; }
  .web { left: 0; width: 405px; top: 911px; text-align: center; color: var(--paper); font-weight: 700; font-size: 22px; letter-spacing: 0.3px; }
</style>
</head>
<body>

<section class="hanger hanger--front">
  <div class="photo photo--lamps" role="img" aria-label="Photo of three glowing cube pendant lamps on a dark ceiling"></div>
  <div class="door-hole"></div>
  <div class="brand brand--light">K&amp;T Electric, LLC</div>
  <h1 class="band headline front-headline">Need a Reliable<br>Electrician?</h1>
  <h2 class="subhead">Your Local Electrical Expert<br>is Just Around the Corner!</h2>
  <div class="photo photo--worker" role="img" aria-label="Photo of a smiling electrician in a hard hat and blue overalls carrying cable and a tool bag"></div>
  <ul class="bolt-list benefits">
    <li>Quick Response Times</li>
    <li>Affordable Rates</li>
    <li>Quality Workmanship</li>
    <li>Fully Licensed &amp; Insured</li>
  </ul>
  <p class="offer">Special Offer:<span class="offer-big">10% OFF</span>Your First Service Call!</p>
  <div class="brand brand--dark" style="left:45px;top:765px;z-index:2">K&amp;T Electric, LLC</div>
  <div class="band footer"></div>
  <div class="cta-pill">Call Us Today</div>
  <div class="phone">555-318-4702</div>
  <div class="web-label">Visit Our Website:</div>
  <div class="web">www.kandtelectric.example</div>
</section>

<section class="hanger hanger--back">
  <div class="photo photo--panel" role="img" aria-label="Photo of gloved hands working on wires in an electrical panel"></div>
  <div class="door-hole"></div>
  <h1 class="band headline back-headline">Don't Let Electrical<br>Issues Keep<br>You in the Dark!</h1>
  <p class="intro">From flickering lights to complete<br>system upgrades, we've got all your<br>residential electrical needs covered.</p>
  <h3 class="services-title">Our services include:</h3>
  <ul class="bolt-list services">
    <li>Electrical Repairs &amp; Troubleshooting</li>
    <li>Lighting Installation &amp; Upgrades</li>
    <li>Safety Inspections &amp; Code Compliance</li>
    <li>Energy-Efficient Solutions</li>
    <li>24/7 Emergency Services</li>
  </ul>
  <div class="photo photo--bulbs" role="img" aria-label="Photo of hanging vintage filament light bulbs"></div>
  <p class="why">Why Choose Us?<br>Friendly, Local Service<br>Over 30 Years of Experience</p>
  <div class="brand brand--dark" style="left:31px;top:765px">K&amp;T Electric, LLC</div>
  <p class="booking">Book Your Appointment Now<br>and Claim Your <span class="offer-big">10% OFF</span></p>
  <p class="fine-print">Offer valid for new customers on the first visit only.<br>Mention this door hanger when booking.</p>
  <div class="band footer"></div>
  <div class="cta-pill">Call Us Today</div>
  <div class="phone">555-318-4702</div>
  <div class="web-label">Visit Our Website:</div>
  <div class="web">www.kandtelectric.example</div>
</section>

</body>
</html>
```